I would like to modify/update my 2 step login screen

I want a more modern looking login page for our document imaging application. I need to keep all of the same elements and buttons that currently exist. The first 2 screens are the login. The 3rd is a screenshot of the actual application home page.

```html
<!DOCTYPE html>
<html lang="en">
<head>
<meta charset="utf-8">
<title>Meridian Works – Login Screens</title>
<link href="https://fonts.googleapis.com/css2?family=Questrial&display=swap" rel="stylesheet">
<style>
  :root{
    --bg:#000000;
    --white:#ffffff;
    --green:#5cb85c;
    --green-mid:#3f9a4c;
    --green-deep:#256f38;
    --green-dark:#1f6431;
    --field:#addcad;
    --field-text:#6f9f72;
    --ink:#1a1a1a;
    --pill-ink:#1c5a2b;
  }
  *{box-sizing:border-box;margin:0;padding:0}
  html,body{width:1084px;height:1200px;overflow:hidden;background:var(--bg)}
  body{position:relative;font-family:"Questrial",sans-serif}
  .art{position:absolute;left:0;top:0}
  .abs{position:absolute;white-space:nowrap}
  .center{text-align:center}
  .brand{color:var(--white);font-size:15px;letter-spacing:.5px;display:flex;align-items:center;gap:7px;white-space:nowrap}
  .brand-dot{width:12px;height:12px;border-radius:50%;background:var(--white)}
  .heading{-webkit-text-stroke:.7px currentColor}
  .hello-white{color:var(--white)}
  .hello-green{color:var(--green)}
  .sub{color:var(--ink)}
  .pill{position:absolute;border-radius:20px;display:flex;align-items:center;justify-content:center;font-size:12px;white-space:nowrap}
  .pill-outline{border:1px solid rgba(255,255,255,.8);color:var(--pill-ink)}
  .pill-soft{background:var(--green);color:var(--pill-ink)}
  .pill-icon{position:absolute;left:8px;top:50%;transform:translateY(-50%);width:14px;height:14px;border-radius:50%;background:var(--white)}
  .field{background:var(--field);color:var(--field-text)}
  .action{background:var(--green);color:var(--white)}
  .outline-white{border:1px solid var(--white);color:var(--white)}
  .footer-links{color:var(--white);font-size:7px;-webkit-text-stroke:.2px currentColor}
  .footer-copy{color:rgba(255,255,255,.8);font-size:5.5px}
  .forgot{color:var(--ink)}
</style>
</head>
<body>

<svg class="art" width="1084" height="1200" viewBox="0 0 1084 1200" aria-hidden="true">
  <defs>
    <linearGradient id="panelGreen" x1="0" y1="0" x2="0" y2="1">
      <stop offset="0" stop-color="#2f8440"/>
      <stop offset="1" stop-color="#5cb85c"/>
    </linearGradient>
    <linearGradient id="panelShade" x1="0" y1="0" x2="1" y2="0">
      <stop offset="0" stop-color="#5cb85c"/>
      <stop offset="1" stop-color="#1f6431"/>
    </linearGradient>
    <linearGradient id="cornerGreen" x1="0" y1="0" x2="1" y2="0">
      <stop offset="0" stop-color="#2b7d3c"/>
      <stop offset="1" stop-color="#5cb85c"/>
    </linearGradient>
    <linearGradient id="phoneGreen" x1="0" y1="0" x2="0" y2="1">
      <stop offset="0" stop-color="#5cb85c"/>
      <stop offset="1" stop-color="#206a34"/>
    </linearGradient>
    <linearGradient id="circleGreen" x1="0" y1="0" x2="0" y2="1">
      <stop offset="0" stop-color="#2b7d3c"/>
      <stop offset="1" stop-color="#5cb85c"/>
    </linearGradient>
    <clipPath id="desktopClip"><rect x="93" y="101" width="894" height="432" rx="30"/></clipPath>
    <clipPath id="phoneClip"><rect x="606" y="663" width="216" height="431" rx="16"/></clipPath>
  </defs>

  <!-- desktop card -->
  <g clip-path="url(#desktopClip)">
    <rect x="93" y="101" width="894" height="432" fill="#ffffff"/>
    <rect x="330" y="300" width="155" height="233" fill="url(#panelShade)"/>
    <circle cx="225" cy="285" r="262" fill="url(#panelGreen)"/>
    <path d="M250 545 A262 262 0 0 0 485 300 L485 545 Z" fill="url(#panelShade)"/>
    <path d="M875 101 L987 101 L987 280 Q965 150 875 101 Z" fill="url(#cornerGreen)"/>
  </g>

  <!-- mobile welcome -->
  <rect x="258" y="663" width="215" height="431" rx="16" fill="url(#phoneGreen)"/>

  <!-- mobile login -->
  <g clip-path="url(#phoneClip)">
    <rect x="606" y="663" width="216" height="431" fill="#ffffff"/>
    <path d="M606 663 L650 663 Q615 700 606 760 Z" fill="url(#cornerGreen)"/>
    <path d="M760 862 L822 862 L822 760 Q810 840 760 862 Z" fill="url(#panelShade)"/>
    <circle cx="714" cy="754" r="108" fill="url(#circleGreen)"/>
    <path d="M606 1030 Q615 1075 650 1094 L606 1094 Z" fill="url(#cornerGreen)"/>
  </g>
</svg>

<!-- desktop: left panel -->
<div class="abs brand" style="left:182px;top:138px"><span class="brand-dot"></span>MERIDIAN WORKS</div>
<div class="abs hello-white heading" style="left:128px;top:195px;font-size:30px">Welcome MRDN!</div>

<div class="pill pill-outline" style="left:145px;top:246px;width:195px;height:28px">Database</div>
<div class="pill pill-soft" style="left:145px;top:292px;width:195px;height:28px"><span class="pill-icon"></span>Log in with myMRView</div>
<div class="pill pill-outline" style="left:145px;top:339px;width:195px;height:28px"><span class="pill-icon"></span>Log in with Gallop</div>
<div class="pill pill-outline" style="left:145px;top:386px;width:195px;height:28px"><span class="pill-icon"></span>Log in with Microvane</div>
<div class="pill pill-outline" style="left:145px;top:433px;width:195px;height:28px"><span class="pill-icon"></span>Log in with Quillgate</div>

<div class="abs footer-links center" style="left:143px;top:487px;width:200px">Privacy | Remote Support | Contact Us</div>
<div class="abs footer-copy center" style="left:143px;top:499px;width:200px">Copyright 2001-2024 Meridian Works</div>

<!-- desktop: right panel -->
<div class="abs hello-green heading center" style="left:586px;top:126px;width:300px;font-size:32px">Welcome Classic!</div>
<div class="abs sub center" style="left:586px;top:165px;width:300px;font-size:13px">Login in to your account to continue</div>

<div class="pill field" style="left:588px;top:244px;width:296px;height:38px;border-radius:19px">Username</div>
<div class="pill field" style="left:588px;top:301px;width:296px;height:40px;border-radius:20px">Password</div>
<div class="pill action" style="left:588px;top:359px;width:296px;height:38px;border-radius:19px">Log in to MRDNDEMO23</div>
<div class="abs forgot center" style="left:586px;top:410px;width:300px;font-size:9px">Forgot your password?</div>
<div class="pill action" style="left:672px;top:485px;width:129px;height:25px">LOGIN</div>

<!-- mobile welcome -->
<div class="abs brand" style="left:316px;top:766px;font-size:12px;gap:5px"><span class="brand-dot" style="width:10px;height:10px"></span>MERIDIAN WORKS</div>
<div class="abs hello-white heading center" style="left:258px;top:870px;width:215px;font-size:20px">Welcome MRDN!</div>
<div class="pill outline-white" style="left:289px;top:974px;width:154px;height:23px;font-size:10px">LOGIN</div>

<!-- mobile login -->
<div class="abs brand" style="left:666px;top:744px;font-size:12px;gap:5px"><span class="brand-dot" style="width:10px;height:10px"></span>MERIDIAN WORKS</div>
<div class="abs hello-green heading center" style="left:606px;top:893px;width:216px;font-size:18px">Welcome Classic!</div>
<div class="abs sub center" style="left:606px;top:915px;width:216px;font-size:7px">Login in to your account to continue</div>
<div class="pill field" style="left:629px;top:961px;width:170px;height:22px;font-size:7px">Username</div>
<div class="pill field" style="left:629px;top:994px;width:170px;height:22px;font-size:7px">Password</div>
<div class="pill action" style="left:629px;top:1027px;width:170px;height:22px;font-size:7px">Log in to MRDNDEMO23</div>
<div class="abs forgot center" style="left:606px;top:1055px;width:216px;font-size:6px">Forgot your password?</div>

</body>
</html>
```